Präsentationsvorlagen für Unternehmensberater
Zielgruppe
Ich bin selbstständiger Unternehmensberater / Freelancer / Projektmanager / Interimmanager und Trainer in den Bereichen operative Logistik und Logistik-IT. Meine Kundenmix reicht vom Kleinunternehmen bis hin zu multinationalen Konzernen. Meine Projekte führen mich nach ganz Europa, mit Schwerpunkten im Osten. Als Projektsprachen verwende ich deutsch und englisch.
Aufgabenstellung
Ich suche nach einem umfangreichen Powerpoint-Masterfile zur Verwendung sowohl in der Aquisitionsphase als auch in den Projekten. Das moderne Design muss am Corporate Design angelehnt sein (siehe beiliegende Dateien, Webpage ist noch in Entwicklung, die aktuelle Layoutplanung ist aber verfügbar und kann bei Bedarf übermittelt werden). Geschwungene Formen bevorzuge ich gegenüber gradliniger Geometrie. Ein wenig verspielt darf es sein, ohne jedoch an Professionalität einzubüßen.
Folgendes soll im Masterfile berücksichtigt werden:
Aufbau:
- Dreistufige Struktur (Titel / Bereich / Thema)
- verborgene Folien / direkter Klick auf Themen z.B. von Inhaltsverzeichnis werden genutzt
- Animationen werden verwendet
- Seitenverhältnis 16:9
aktuell geplante Folientypen (Vorlage für alle Typen gewünscht):
- Agenda
- Übersicht / Inhalt
- Text/Aufzählung
- Zeitleiste
- Bilder mit/ohne Textspalte
- eingebundenes Video mit/ohne Text
- Darstellung ineinandergreifender Themen (ähnlich Puzzle)
- Diagramme (Kreisdiagramm, Balkendiagramm, Liniendiagramm, Spiderweb) jeweils mit und ohne Textspalte
- Gegenüberstellungen (z.B. Vor- und Nachteile)
- Wordcloud
- Prozessschritte
- Flowcharts
- Tabellen
- magisches Dreick/Vieleck (Darstellung untereinander konkurrierenden Ziele)
- Slogans / Zitate / Hypothesen
- Mengenüberschneidungen
- Call to Action
- Schlussfolie / Fragen?
- Kontaktdaten

```html
<!DOCTYPE html>
<html lang="de">
<head>
<meta charset="utf-8">
<title>Velmoro – Präsentationsvorlage</title>
<link href="https://fonts.googleapis.com/css2?family=Ubuntu:wght@300;400;500;700&family=Lato:wght@300;400;700&display=swap" rel="stylesheet">
<style>
:root{
  --blue:#27a7e0;
  --cyan:#00bff3;
  --deep:#1b9ad6;
  --dark:#555;
  --mid:#8c8c8c;
  --soft:#b5b5b5;
  --pale:#dedede;
  --band:#6e6e6e;
  --ink:#2f2f2f;
  --muted:#9b9b9b;
  --page:#dcdcdc;
  --white:#fff;
}
*{box-sizing:border-box;margin:0;padding:0}
html,body{width:1200px;height:2964px;overflow:hidden;background:var(--page)}
body{font-family:"Lato",sans-serif;color:var(--ink)}
.deck{position:absolute;left:76px;top:66px;display:grid;grid-template-columns:524px 524px;grid-auto-rows:293px;column-gap:21px;row-gap:23px}
.slide{position:relative;background:var(--white);overflow:hidden}
.wave{position:absolute;left:0;bottom:0;width:100%;height:80px}
.date{position:absolute;left:10px;top:12px;font-size:6px;letter-spacing:2.4px;color:var(--muted)}
.badge{position:absolute;right:8px;top:7px;width:21px;height:21px;border-radius:50%;border:2px solid var(--blue)}
.pageno,.url{position:absolute;bottom:8px;font-size:6px;letter-spacing:2.6px;color:var(--white)}
.pageno{left:10px}
.url{right:10px}
.title{position:absolute;left:0;right:0;top:36px;text-align:center;font-family:"Ubuntu",sans-serif;font-weight:500;font-size:17px;color:var(--ink)}
.lead{position:absolute;left:92px;right:92px;top:71px;text-align:center;font-size:5.2px;line-height:1.6;color:var(--muted)}
.tiny{font-size:5px;line-height:1.6;color:var(--muted)}
.abs{position:absolute}
.ph{position:absolute;display:block}

/* cover */
.cover-top{position:absolute;left:0;top:0;width:524px;height:110px}
.brand{position:absolute;left:0;right:0;top:118px;display:flex;justify-content:center;align-items:center;gap:10px}
.brand-dot{width:62px;height:62px;border-radius:50%;border:5px solid var(--blue)}
.brand-name{font-family:"Ubuntu",sans-serif;font-weight:500;font-size:36px;color:var(--blue);line-height:1}
.brand-sub{font-family:"Ubuntu",sans-serif;font-weight:500;font-size:9px;letter-spacing:2.4px;color:var(--blue);margin-top:3px}
.cover-wave{position:absolute;left:0;bottom:0;width:100%;height:90px}
.cover-url{position:absolute;left:0;right:0;bottom:22px;text-align:center;font-size:6px;letter-spacing:3px;color:var(--white)}

/* agenda */
.band{position:absolute;left:0;right:0;top:105px;height:95px;background:var(--band)}
.agenda-item{position:absolute;top:136px;display:flex;align-items:center;gap:14px}
.agenda-item p{font-size:5px;line-height:1.6;color:var(--white);width:70px}
.ico{width:32px;height:32px;border-radius:50%;display:flex;align-items:center;justify-content:center;flex:none}
.ico svg{width:13px;height:13px}
.ico.blue{background:var(--blue)}
.ico.grey{background:var(--soft)}
.ico.dark{background:var(--dark)}
.agenda-foot{top:218px}

/* overview */
.overview{position:absolute;left:88px;right:88px;top:72px;text-align:center}
.overview p{font-size:5.2px;line-height:1.65;color:var(--muted);margin-bottom:9px}

/* timeline */
.tl-line{position:absolute;left:0;right:0;top:207px;height:1px;background:var(--pale)}
.tl-dot{position:absolute;top:203px;width:9px;height:9px;border-radius:50%}
.tl-stem{position:absolute;width:1px;background:var(--pale)}
.tl-pic{position:absolute;width:24px;height:26px;background:linear-gradient(180deg,#d8d8d8,#8e8e8e)}
.tl-text{position:absolute;width:78px}
.tl-text h4{font-family:"Ubuntu",sans-serif;font-weight:500;font-size:8px;color:var(--ink);margin-bottom:3px}
.tl-foot{top:228px}

/* text column */
.col h3{font-family:"Ubuntu",sans-serif;font-weight:400;font-size:14.5px;line-height:1.2;color:var(--ink);margin-bottom:9px}
.col h3 b{font-weight:500}
.col p{font-size:5px;line-height:1.7;color:var(--muted);margin-bottom:6px}
.video{position:absolute;background:#000}
.video .ph{left:0;right:0;top:12%;bottom:12%}
.photo-title{color:var(--white);font-weight:400}

/* charts */
.pie{position:absolute;border-radius:50%}
.pie-label{position:absolute;font-size:6px;color:var(--white)}
.legend{position:absolute;display:flex;gap:7px;font-size:5px;color:var(--dark)}
.legend i{display:inline-block;width:4px;height:4px;margin-right:2px;vertical-align:middle}
.donut-lbl{position:absolute;width:80px}
.donut-lbl h4{font-family:"Ubuntu",sans-serif;font-weight:500;font-size:8px;margin-bottom:3px}
.donut-lbl.r{text-align:left}
.donut-lbl.l{text-align:right}
.num{position:absolute;font-size:7px;color:var(--white)}
.btn{display:inline-block;margin-top:4px;padding:3px 10px;border-radius:6px;background:var(--dark);color:var(--white);font-size:5px}
.side{position:absolute;left:93px;top:114px;width:150px}
.side .kicker{font-size:6px;color:var(--soft);margin-bottom:1px}
.side h3{font-family:"Ubuntu",sans-serif;font-weight:400;font-size:14px;color:var(--ink);margin-bottom:9px}
.side p{font-size:4.8px;line-height:1.7;color:var(--muted);margin-bottom:6px}
.stat{position:absolute;left:282px;top:212px;display:flex;gap:8px;align-items:flex-start}
.stat strong{font-family:"Ubuntu",sans-serif;font-weight:500;font-size:23px;color:var(--dark);line-height:1}
.stat strong small{font-size:9px}
.stat h5{font-family:"Ubuntu",sans-serif;font-weight:500;font-size:6px;margin-bottom:2px}
.stat p{font-size:4.6px;line-height:1.6;color:var(--muted);width:70px}
.bars{position:absolute;display:flex;align-items:flex-end;border-bottom:1px solid var(--pale)}
.bar{position:relative;flex:1}
.bar span{position:absolute;left:0;right:0;top:-9px;text-align:center;font-size:5px;color:var(--muted)}
.axis{position:absolute;display:flex;font-size:4.6px;color:var(--muted)}
.axis span{flex:1;text-align:center}

/* comparison */
.cmp-head{position:absolute;top:72px;width:110px;text-align:center;font-family:"Ubuntu",sans-serif;font-size:13px;color:var(--dark);border-bottom:2px solid var(--blue);padding-bottom:2px}
.cmp-row{position:absolute;display:flex;gap:12px;align-items:flex-start}
.cmp-row h4{font-family:"Ubuntu",sans-serif;font-weight:500;font-size:8px;margin-bottom:2px}
.cmp-row p{font-size:4.6px;line-height:1.6;color:var(--muted);width:115px}
.cmp-row .ico{width:30px;height:30px}
</style>
</head>
<body>
<svg width="0" height="0" style="position:absolute" aria-hidden="true">
  <defs>
    <symbol id="wave" viewBox="0 0 524 80" preserveAspectRatio="none">
      <path d="M0 58 C90 48 150 66 260 52 C370 38 450 28 524 24 V80 H0Z" fill="#27a7e0"/>
    </symbol>
    <symbol id="i-clip" viewBox="0 0 16 16"><rect x="3" y="2" width="10" height="13" rx="1" fill="#fff"/><rect x="5" y="6" width="6" height="1.2" fill="#27a7e0"/><rect x="5" y="9" width="6" height="1.2" fill="#27a7e0"/></symbol>
    <symbol id="i-card" viewBox="0 0 16 16"><rect x="2" y="3" width="12" height="10" rx="1" fill="#fff"/><circle cx="8" cy="7" r="2" fill="#27a7e0"/><rect x="5" y="10" width="6" height="1.5" fill="#27a7e0"/></symbol>
    <symbol id="i-case" viewBox="0 0 16 16"><rect x="2" y="5" width="12" height="9" rx="1" fill="#fff"/><rect x="6" y="2.5" width="4" height="3" fill="none" stroke="#fff" stroke-width="1.2"/><rect x="7" y="8" width="2" height="2" fill="#888"/></symbol>
    <symbol id="i-cal" viewBox="0 0 16 16"><rect x="2" y="3" width="12" height="11" rx="1" fill="none" stroke="#fff" stroke-width="1.4"/><path d="M5 9 l2 2 l4 -4" fill="none" stroke="#fff" stroke-width="1.4"/></symbol>
  </defs>
</svg>

<main class="deck">

  <!-- 01 cover -->
  <section class="slide cover">
    <svg class="cover-top" viewBox="0 0 524 110" preserveAspectRatio="none" aria-hidden="true"><path d="M0 0 H300 C268 6 270 40 266 60 C262 82 240 86 200 86 H0Z" fill="#27a7e0"/></svg>
    <div class="brand">
      <div class="brand-dot"></div>
      <div>
        <div class="brand-name">Velmoro</div>
        <div class="brand-sub">CONSULTING SERVICES</div>
      </div>
    </div>
    <svg class="cover-wave" viewBox="0 0 524 90" preserveAspectRatio="none" aria-hidden="true"><path d="M0 28 C140 10 260 28 380 14 C440 8 490 8 524 12 V90 H0Z" fill="#27a7e0"/></svg>
    <div class="cover-url">www.velmoro.at</div>
  </section>

  <!-- 02 agenda -->
  <section class="slide">
    <div class="date">01/02/2020</div><div class="badge"></div>
    <h2 class="title">Agenda</h2>
    <p class="lead">Lorem ipsum dolor sit amet, consectetur adipiscing elit. Curabitur lobortis mauris et velit ultricies, id congue mauris ultricies. Suspendisse pretium, massa ut dictum dictum.</p>
    <div class="band"></div>
    <div class="agenda-item" style="left:51px"><span class="ico blue"><svg><use href="#i-clip"/></svg></span><p>Lorem ipsum dolor sit amet, consectetur adipiscing elit. Curabitur lobortis.</p></div>
    <div class="agenda-item" style="left:199px"><span class="ico blue"><svg><use href="#i-card"/></svg></span><p>Lorem ipsum dolor sit amet, consectetur adipiscing elit. Curabitur lobortis.</p></div>
    <div class="agenda-item" style="left:346px"><span class="ico grey"><svg><use href="#i-case"/></svg></span><p>Lorem ipsum dolor sit amet, consectetur adipiscing elit. Curabitur lobortis.</p></div>
    <p class="lead agenda-foot">Lorem ipsum dolor sit amet, consectetur adipiscing elit. Curabitur lobortis mauris et velit ultricies, id congue mauris ultricies. Suspendisse pretium, massa ut dictum dictum, sapien dui sodales sem, vel commodo libero tellus quis ex.</p>
    <svg class="wave"><use href="#wave"/></svg>
    <span class="pageno">02</span><span class="url">www.velmoro.at</span>
  </section>

  <!-- 03 overview -->
  <section class="slide">
    <div class="date">01/02/2020</div><div class="badge"></div>
    <h2 class="title">Übersicht</h2>
    <div class="overview">
      <p>Lorem ipsum dolor sit amet, consectetur adipiscing elit. Curabitur lobortis mauris et velit ultricies, id congue mauris ultricies. Suspendisse pretium, massa ut dictum dictum, sapien dui sodales sem, vel commodo libero tellus quis ex. Praesent interdum lorem faucibus quis erat tincidunt, ac placerat eros tincidunt. Donec ligula eros, elementum a porta ac, gravida ac dolor. Aenean blandit orci id erat tristique pharetra. Nam posuere purus non ante interdum, a euismod nisl sodales. Sed ac tincidunt urna, nec facilisis sem.</p>
      <p>Praesent id elit sed orci pellentesque tincidunt a vitae nibh. Praesent blandit risus vel quam varius, sit amet ullamcorper eros sagittis. Duis et velit eget orci sodales viverra non vitae arcu. Quisque quis ante id nisl varius eleifend at a ante. Vivamus eget tortor vel nunc efficitur euismod. Pellentesque habitant morbi tristique senectus et netus et malesuada fames ac turpis egestas. Duis vehicula semper sagittis. In lorem nisi, posuere cursus mollis vitae, gravida a elit. Curabitur id ante sit amet magna gravida euismod. Aenean in aliquam massa. Vestibulum ac mi nec metus fermentum laoreet vitae convallis tellus. Phasellus tincidunt ligula ut augue semper imperdiet. Fusce egestas felis sed diam sollicitudin mattis.</p>
      <p>Donec nec augue leo. Vestibulum interdum ipsum et bibendum eleifend. Etiam congue dui vitae sagittis volutpat. Fusce convallis blandit enim, vitae faucibus dolor ultricies eu. Morbi malesuada venenatis enim vitae faucibus. Integer aliquam ullamcorper accumsan. Morbi pulvinar in ipsum in pharetra. Sed et lacus, tempor quis elit eu, vulputate pulvinar justo.</p>
    </div>
    <svg class="wave"><use href="#wave"/></svg>
    <span class="pageno">03</span><span class="url">www.velmoro.at</span>
  </section>

  <!-- 04 timeline -->
  <section class="slide">
    <div class="date">01/02/2020</div><div class="badge"></div>
    <h2 class="title">Zeitleiste</h2>
    <p class="lead">Lorem ipsum dolor sit amet, consectetur adipiscing elit. Curabitur lobortis mauris et velit ultricies, id congue mauris ultricies. Suspendisse pretium, massa ut dictum dictum.</p>
    <div class="tl-line"></div>
    <div class="tl-stem" style="left:67px;top:150px;height:55px"></div>
    <div class="tl-stem" style="left:182px;top:123px;height:82px"></div>
    <div class="tl-stem" style="left:298px;top:150px;height:55px"></div>
    <div class="tl-stem" style="left:408px;top:123px;height:82px"></div>
    <span class="tl-pic" role="img" aria-label="Porträtfoto einer Mitarbeiterin" style="left:55px;top:124px"></span>
    <span class="tl-pic" role="img" aria-label="Porträtfoto eines Mitarbeiters" style="left:170px;top:97px"></span>
    <span class="tl-pic" role="img" aria-label="Porträtfoto eines Mitarbeiters" style="left:286px;top:124px"></span>
    <span class="tl-pic" role="img" aria-label="Porträtfoto einer Mitarbeiterin" style="left:396px;top:97px"></span>
    <div class="tl-text" style="left:86px;top:140px"><h4>Pellentesque</h4><p class="tiny">Lorem ipsum dolor sit amet, consectetur adipiscing elit. Curabitur lobortis mauris et velit ultricies, id congue.</p></div>
    <div class="tl-text" style="left:201px;top:113px"><h4>Tincidunt</h4><p class="tiny">Lorem ipsum dolor sit amet, consectetur adipiscing elit. Curabitur lobortis mauris et velit ultricies, id congue.</p></div>
    <div class="tl-text" style="left:318px;top:140px"><h4>Praesent blandit</h4><p class="tiny">Lorem ipsum dolor sit amet, consectetur adipiscing elit. Curabitur lobortis mauris et velit ultricies, id congue.</p></div>
    <div class="tl-text" style="left:430px;top:113px"><h4>Ullamcorper</h4><p class="tiny">Lorem ipsum dolor sit amet, consectetur adipiscing elit. Curabitur lobortis mauris et velit ultricies, id congue.</p></div>
    <span class="tl-dot" style="left:58px;background:var(--cyan)"></span>
    <span class="tl-dot" style="left:174px;background:var(--deep)"></span>
    <span class="tl-dot" style="left:289px;background:var(--dark)"></span>
    <span class="tl-dot" style="left:399px;background:var(--mid)"></span>
    <p class="lead tl-foot">Lorem ipsum dolor sit amet, consectetur adipiscing elit. Curabitur lobortis mauris et velit ultricies, id congue mauris ultricies. Suspendisse pretium, massa ut dictum dictum, sapien dui sodales sem, vel commodo libero tellus quis ex.</p>
    <svg class="wave"><use href="#wave"/></svg>
    <span class="pageno">04</span><span class="url">www.velmoro.at</span>
  </section>

  <!-- 05 images with text -->
  <section class="slide">
    <div class="date">01/02/2020</div><div class="badge"></div>
    <h2 class="title">Bilder mit Textspalte</h2>
    <p class="lead">Lorem ipsum dolor sit amet, consectetur adipiscing elit. Curabitur lobortis mauris et velit ultricies, id congue mauris ultricies. Suspendisse pretium, massa ut dictum dictum.</p>
    <span class="ph" role="img" aria-label="Foto: Team bespricht Pläne am Besprechungstisch" style="left:94px;top:108px;width:144px;height:185px;background:linear-gradient(160deg,#e9e4dc 0%,#b9a898 45%,#5d5f66 100%)"></span>
    <div class="abs col" style="left:267px;top:113px;width:175px">
      <h3>Vestibulum interdum ipsum <b>et bibendum eleifend. Etiam</b></h3>
      <p>Praesent id elit sed orci pellentesque tincidunt a vitae nibh. Praesent blandit risus vel quam varius, sit amet ullamcorper.</p>
      <p>Donec nec augue leo. Vestibulum interdum ipsum et bibendum eleifend. Etiam congue dui vitae sagittis volutpat. Fusce convallis blandit enim, vitae faucibus dolor ultricies eu. Morbi malesuada venenatis enim vitae faucibus. Integer aliquam ullamcorper accumsan.</p>
    </div>
    <svg class="wave"><use href="#wave"/></svg>
    <span class="pageno">05</span><span class="url">www.velmoro.at</span>
  </section>

  <!-- 06 images without text -->
  <section class="slide">
    <span class="ph" role="img" aria-label="Foto: Skyline mit Hochhäusern und herbstlichen Bäumen" style="inset:0;background:linear-gradient(180deg,#2a62c9 0%,#6d95d8 38%,#c7ccd2 58%,#8f8a80 75%,#b96f2e 90%,#5c6a3a 100%)"></span>
    <div class="date" style="color:var(--white)">01/02/2020</div><div class="badge" style="border-color:var(--white)"></div>
    <h2 class="title photo-title">Bilder ohne Textspalte</h2>
    <svg class="wave"><use href="#wave"/></svg>
    <span class="pageno">06</span><span class="url">www.velmoro.at</span>
  </section>

  <!-- 07 video with text -->
  <section class="slide">
    <div class="date">01/02/2020</div><div class="badge"></div>
    <h2 class="title">Eingebundenes Video mit Text</h2>
    <div class="video" style="left:28px;top:80px;width:273px;height:154px">
      <span class="ph" role="img" aria-label="Video: Skyline einer Großstadt bei Tag" style="background:linear-gradient(180deg,#4f7fa6 0%,#b8cbd9 50%,#8b8b84 80%,#5a574f 100%)"></span>
    </div>
    <div class="abs col" style="left:322px;top:78px;width:180px">
      <h3>Vestibulum interdum ipsum <b>et bibendum eleifend. Etiam</b></h3>
      <p>Praesent id elit sed orci pellentesque tincidunt a vitae nibh. Praesent blandit risus vel quam varius, sit amet ullamcorper.</p>
      <p>Donec nec augue leo. Vestibulum interdum ipsum et bibendum eleifend. Etiam congue dui vitae sagittis volutpat. Fusce convallis blandit enim, vitae faucibus dolor ultricies eu. Morbi malesuada venenatis enim vitae faucibus. Integer aliquam ullamcorper accumsan.</p>
    </div>
    <svg class="wave"><use href="#wave"/></svg>
    <span class="pageno">07</span><span class="url">www.velmoro.at</span>
  </section>

  <!-- 08 video without text -->
  <section class="slide">
    <div class="date">01/02/2020</div><div class="badge"></div>
    <h2 class="title">Eingebundenes Video ohne Text</h2>
    <div class="video" style="left:113px;top:66px;width:299px;height:168px">
      <span class="ph" role="img" aria-label="Video: Skyline einer Großstadt bei Tag" style="background:linear-gradient(180deg,#4f7fa6 0%,#b8cbd9 50%,#8b8b84 80%,#5a574f 100%)"></span>
    </div>
    <svg class="wave"><use href="#wave"/></svg>
    <span class="pageno">08</span><span class="url">www.velmoro.at</span>
  </section>

  <!-- 09 interlocking topics -->
  <section class="slide">
    <div class="date">01/02/2020</div><div class="badge"></div>
    <h2 class="title">Darstellung ineinandergreifender Themen</h2>
    <p class="lead">Lorem ipsum dolor sit amet, consectetur adipiscing elit. Curabitur lobortis mauris et velit ultricies, id congue mauris ultricies. Suspendisse pretium, massa ut dictum dictum.</p>
    <div class="pie" style="left:203px;top:97px;width:124px;height:124px;background:conic-gradient(var(--cyan) 0 89deg,#fff 89deg 91deg,var(--deep) 91deg 179deg,#fff 179deg 181deg,var(--dark) 181deg 269deg,#fff 269deg 271deg,var(--mid) 271deg 359deg,#fff 359deg)"></div>
    <div class="pie" style="left:234px;top:128px;width:62px;height:62px;background:#fff"></div>
    <span class="num" style="left:229px;top:122px">01</span>
    <span class="num" style="left:291px;top:122px">02</span>
    <span class="num" style="left:291px;top:188px">03</span>
    <span class="num" style="left:229px;top:188px">04</span>
    <div class="donut-lbl l" style="left:66px;top:111px"><h4>Hendrerit viverra</h4><p class="tiny">Donec nec augue leo. Vestibulum interdum ipsum et bibendum eleifend. Etiam congue dui vitae sagittis volutpat.</p></div>
    <div class="donut-lbl l" style="left:66px;top:177px"><h4>Maecenas venenatis</h4><p class="tiny">Donec nec augue leo. Vestibulum interdum ipsum et bibendum eleifend. Etiam congue dui vitae sagittis volutpat.</p></div>
    <div class="donut-lbl r" style="left:378px;top:110px"><h4>Vestibulum interdum</h4><p class="tiny">Donec nec augue leo. Vestibulum interdum ipsum et bibendum eleifend. Etiam congue dui vitae sagittis volutpat.</p></div>
    <div class="donut-lbl r" style="left:378px;top:177px"><h4>Aenean quis</h4><p class="tiny">Donec nec augue leo. Vestibulum interdum ipsum et bibendum eleifend. Etiam congue dui vitae sagittis volutpat.</p></div>
    <svg class="abs" style="left:0;top:0" width="524" height="293" aria-hidden="true">
      <g stroke="#cfcfcf" stroke-width=".6"><line x1="166" y1="132" x2="200" y2="132"/><line x1="166" y1="198" x2="200" y2="198"/><line x1="330" y1="132" x2="372" y2="132"/><line x1="330" y1="198" x2="372" y2="198"/></g>
    </svg>
    <svg class="wave"><use href="#wave"/></svg>
    <span class="pageno">09</span><span class="url">www.velmoro.at</span>
  </section>

  <!-- 10 pie with text -->
  <section class="slide">
    <div class="date">01/02/2020</div><div class="badge"></div>
    <h2 class="title">Kreisdiagramm mit text</h2>
    <p class="lead">Lorem ipsum dolor sit amet, consectetur adipiscing elit. Curabitur lobortis mauris et velit ultricies, id congue mauris ultricies. Suspendisse pretium, massa ut dictum dictum.</p>
    <div class="pie" style="left:88px;top:99px;width:142px;height:142px;background:conic-gradient(var(--deep) 0 137deg,var(--cyan) 137deg 240deg,#e4e4e4 240deg 281deg,var(--soft) 281deg 312deg,var(--mid) 312deg 339deg,var(--dark) 339deg)"></div>
    <span class="pie-label" style="left:204px;top:140px">39%</span>
    <span class="pie-label" style="left:150px;top:224px">30%</span>
    <span class="pie-label" style="left:95px;top:178px;color:var(--dark)">12%</span>
    <span class="pie-label" style="left:99px;top:148px">9%</span>
    <span class="pie-label" style="left:115px;top:120px">8%</span>
    <span class="pie-label" style="left:138px;top:104px">7%</span>
    <div class="legend" style="left:78px;top:249px"><span><i style="background:var(--deep)"></i>February</span><span><i style="background:var(--cyan)"></i>March</span><span><i style="background:#e4e4e4"></i>April</span><span><i style="background:var(--soft)"></i>May</span><span><i style="background:var(--mid)"></i>June</span><span><i style="background:var(--dark)"></i>July</span></div>
    <div class="abs col" style="left:310px;top:118px;width:170px">
      <h3 style="font-size:9px;font-weight:500;margin-bottom:5px">Hendrerit viverra</h3>
      <p>Praesent id elit sed orci pellentesque tincidunt a vitae nibh. Praesent blandit risus vel quam varius, sit amet ullamcorper.</p>
      <p>Donec nec augue leo. Vestibulum interdum ipsum et bibendum eleifend. Etiam congue dui vitae sagittis volutpat. Fusce convallis blandit enim, vitae faucibus dolor ultricies eu. Morbi malesuada venenatis enim vitae faucibus. Integer aliquam ullamcorper accumsan.</p>
      <span class="btn">learn more</span>
    </div>
    <svg class="wave"><use href="#wave"/></svg>
    <span class="pageno">10</span><span class="url">www.velmoro.at</span>
  </section>

  <!-- 11 pie without text -->
  <section class="slide">
    <div class="date">01/02/2020</div><div class="badge"></div>
    <h2 class="title">Kreisdiagramm ohne Text</h2>
    <div class="pie" style="left:187px;top:79px;width:150px;height:150px;background:conic-gradient(var(--deep) 0 137deg,var(--cyan) 137deg 240deg,#e4e4e4 240deg 281deg,var(--soft) 281deg 312deg,var(--mid) 312deg 339deg,var(--dark) 339deg)"></div>
    <span class="pie-label" style="left:310px;top:122px">39%</span>
    <span class="pie-label" style="left:254px;top:214px">30%</span>
    <span class="pie-label" style="left:196px;top:167px;color:var(--dark)">12%</span>
    <span class="pie-label" style="left:199px;top:136px">9%</span>
    <span class="pie-label" style="left:217px;top:106px">8%</span>
    <span class="pie-label" style="left:242px;top:88px">7%</span>
    <div class="legend" style="left:178px;top:236px"><span><i style="background:var(--deep)"></i>February</span><span><i style="background:var(--cyan)"></i>March</span><span><i style="background:#e4e4e4"></i>April</span><span><i style="background:var(--soft)"></i>May</span><span><i style="background:var(--mid)"></i>June</span><span><i style="background:var(--dark)"></i>July</span></div>
    <svg class="wave"><use href="#wave"/></svg>
    <span class="pageno">11</span><span class="url">www.velmoro.at</span>
  </section>

  <!-- 12 bar with text -->
  <section class="slide">
    <div class="date">01/02/2020</div><div class="badge"></div>
    <h2 class="title">Kreisdiagramm mit text</h2>
    <p class="lead">Lorem ipsum dolor sit amet, consectetur adipiscing elit. Curabitur lobortis mauris et velit ultricies, id congue mauris ultricies. Suspendisse pretium, massa ut dictum dictum.</p>
    <div class="side">
      <div class="kicker">Consectetur adipiscing elit</div>
      <h3>Hendrerit viverra</h3>
      <p>Praesent id elit sed orci pellentesque tincidunt a vitae nibh. Praesent blandit risus vel quam varius, sit amet ullamcorper.</p>
      <p>Donec nec augue leo. Vestibulum interdum ipsum et bibendum eleifend. Etiam congue dui vitae sagittis volutpat. Fusce convallis blandit enim, vitae faucibus dolor ultricies eu. Morbi malesuada venenatis enim vitae faucibus. Integer aliquam ullamcorper accumsan.</p>
    </div>
    <div class="bars" style="left:282px;top:114px;width:140px;height:65px;gap:12px">
      <div class="bar" style="height:100%;background:var(--cyan)"><span>30</span></div>
      <div class="bar" style="height:100%;background:var(--deep)"><span>30</span></div>
      <div class="bar" style="height:93%;background:var(--dark)"><span>28</span></div>
      <div class="bar" style="height:40%;background:var(--mid)"><span>12</span></div>
      <div class="bar" style="height:60%;background:var(--soft)"><span>18</span></div>
    </div>
    <div class="axis" style="left:282px;top:182px;width:140px"><span>1</span><span>2</span><span>3</span><span>4</span><span>5</span></div>
    <div class="stat"><strong>90<small>%</small></strong><div><h5>Projekte insgesamt 2020</h5><p>Ut enim ad minim veniam, quis nostrud exercitation ullamco laboris nisi ut aliquip ex ea commodo.</p></div></div>
    <svg class="wave"><use href="#wave"/></svg>
    <span class="pageno">12</span><span class="url">www.velmoro.at</span>
  </section>

  <!-- 13 bar without text -->
  <section class="slide">
    <div class="date">01/02/2020</div><div class="badge"></div>
    <h2 class="title">Balkendiagramm ohne Text</h2>
    <div class="bars" style="left:160px;top:107px;width:201px;height:100px;gap:18px">
      <div class="bar" style="height:100%;background:var(--cyan)"><span>30</span></div>
      <div class="bar" style="height:100%;background:var(--deep)"><span>30</span></div>
      <div class="bar" style="height:93%;background:var(--dark)"><span>28</span></div>
      <div class="bar" style="height:40%;background:var(--mid)"><span>12</span></div>
      <div class="bar" style="height:48%;background:var(--soft)"><span>18</span></div>
    </div>
    <div class="axis" style="left:160px;top:210px;width:201px"><span>1</span><span>2</span><span>3</span><span>4</span><span>5</span></div>
    <svg class="wave"><use href="#wave"/></svg>
    <span class="pageno">13</span><span class="url">www.velmoro.at</span>
  </section>

  <!-- 14 line with text -->
  <section class="slide">
    <div class="date">01/02/2020</div><div class="badge"></div>
    <h2 class="title">Liniendiagramm mit text</h2>
    <p class="lead">Lorem ipsum dolor sit amet, consectetur adipiscing elit. Curabitur lobortis mauris et velit ultricies, id congue mauris ultricies. Suspendisse pretium, massa ut dictum dictum.</p>
    <div class="side">
      <div class="kicker">Consectetur adipiscing elit</div>
      <h3>Hendrerit viverra</h3>
      <p>Praesent id elit sed orci pellentesque tincidunt a vitae nibh. Praesent blandit risus vel quam varius, sit amet ullamcorper.</p>
      <p>Donec nec augue leo. Vestibulum interdum ipsum et bibendum eleifend. Etiam congue dui vitae sagittis volutpat. Fusce convallis blandit enim, vitae faucibus dolor ultricies eu. Morbi malesuada venenatis enim vitae faucibus. Integer aliquam ullamcorper accumsan.</p>
    </div>
    <svg class="abs" style="left:276px;top:108px" width="150" height="80" aria-hidden="true">
      <line x1="0" y1="62" x2="150" y2="62" stroke="#dedede" stroke-width=".8"/>
      <polyline points="4,8 38,8 72,13 110,42 140,36" fill="none" stroke="#00bff3" stroke-width="1.2"/>
      <g font-size="5" fill="#9b9b9b" font-family="Lato,sans-serif"><text x="20" y="7">30</text><text x="50" y="7">30</text><text x="74" y="11">28</text><text x="104" y="48">12</text><text x="142" y="35">18</text>
      <text x="16" y="72">1</text><text x="46" y="72">2</text><text x="76" y="72">3</text><text x="106" y="72">4</text><text x="136" y="72">5</text></g>
    </svg>
    <div class="stat"><strong>90<small>%</small></strong><div><h5>Projekte insgesamt 2020</h5><p>Ut enim ad minim veniam, quis nostrud exercitation ullamco laboris nisi ut aliquip ex ea commodo.</p></div></div>
    <svg class="wave"><use href="#wave"/></svg>
    <span class="pageno">14</span><span class="url">www.velmoro.at</span>
  </section>

  <!-- 15 line without text -->
  <section class="slide">
    <div class="date">01/02/2020</div><div class="badge"></div>
    <h2 class="title">Liniendiagramm ohne Text</h2>
    <svg class="abs" style="left:140px;top:112px" width="250" height="100" aria-hidden="true">
      <line x1="0" y1="80" x2="250" y2="80" stroke="#dedede" stroke-width=".8"/>
      <polyline points="4,12 82,12 124,20 176,56 222,50" fill="none" stroke="#00bff3" stroke-width="1.2"/>
      <g font-size="5" fill="#9b9b9b" font-family="Lato,sans-serif"><text x="28" y="11">30</text><text x="78" y="11">30</text><text x="126" y="18">28</text><text x="176" y="63">12</text><text x="225" y="49">18</text>
      <text x="25" y="92">1</text><text x="73" y="92">2</text><text x="121" y="92">3</text><text x="169" y="92">4</text><text x="217" y="92">5</text></g>
    </svg>
    <svg class="wave"><use href="#wave"/></svg>
    <span class="pageno">15</span><span class="url">www.velmoro.at</span>
  </section>

  <!-- 16 spiderweb with text -->
  <section class="slide">
    <div class="date">01/02/2020</div><div class="badge"></div>
    <h2 class="title">Spiderweb mit text</h2>
    <p class="lead">Lorem ipsum dolor sit amet, consectetur adipiscing elit. Curabitur lobortis mauris et velit ultricies, id congue mauris ultricies. Suspendisse pretium, massa ut dictum dictum.</p>
    <div class="side">
      <div class="kicker">Consectetur adipiscing elit</div>
      <h3>Hendrerit viverra</h3>
      <p>Praesent id elit sed orci pellentesque tincidunt a vitae nibh. Praesent blandit risus vel quam varius, sit amet ullamcorper.</p>
      <p>Donec nec augue leo. Vestibulum interdum ipsum et bibendum eleifend. Etiam congue dui vitae sagittis volutpat. Fusce convallis blandit enim, vitae faucibus dolor ultricies eu. Morbi malesuada venenatis enim vitae faucibus. Integer aliquam ullamcorper accumsan.</p>
    </div>
    <svg class="abs" style="left:290px;top:86px" width="140" height="130" aria-hidden="true">
      <g transform="translate(70,68)">
        <polygon points="0,-44 42,-14 26,36 -26,36 -42,-14" fill="none" stroke="#dedede" stroke-width=".8"/>
        <polygon points="0,-26 25,-8 15,21 -15,21 -25,-8" fill="none" stroke="#dedede" stroke-width=".8"/>
        <polygon points="0,-34 30,-10 10,20 -12,14 -20,-8" fill="#00bff3"/>
        <polygon points="0,-8 12,4 4,18 -20,12 -24,-6" fill="#1b9ad6"/>
      </g>
      <g font-size="5" fill="#555" font-family="Lato,sans-serif"><text x="58" y="10">1/5/2002</text><text x="112" y="54">1/6/2002</text><text x="98" y="116">1/7/2002</text><text x="0" y="116">1/8/2002</text><text x="-12" y="54">1/9/2002</text></g>
    </svg>
    <div class="stat"><strong>90<small>%</small></strong><div><h5>Projekte insgesamt 2020</h5><p>Ut enim ad minim veniam, quis nostrud exercitation ullamco laboris nisi ut aliquip ex ea commodo.</p></div></div>
    <svg class="wave"><use href="#wave"/></svg>
    <span class="pageno">16</span><span class="url">www.velmoro.at</span>
  </section>

  <!-- 17 spiderweb without text -->
  <section class="slide">
    <div class="date">01/02/2020</div><div class="badge"></div>
    <h2 class="title">Spiderweb ohne Text</h2>
    <svg class="abs" style="left:142px;top:62px" width="240" height="200" aria-hidden="true">
      <g transform="translate(120,100)">
        <polygon points="0,-90 86,-28 53,73 -53,73 -86,-28" fill="none" stroke="#dedede" stroke-width=".9"/>
        <polygon points="0,-54 51,-17 32,44 -32,44 -51,-17" fill="none" stroke="#dedede" stroke-width=".9"/>
        <polygon points="0,-72 60,-20 22,44 -26,30 -42,-16" fill="#00bff3"/>
        <polygon points="0,-16 26,8 8,38 -42,26 -50,-12" fill="#1b9ad6"/>
      </g>
      <g font-size="5.5" fill="#555" font-family="Lato,sans-serif"><text x="106" y="6">1/5/2002</text><text x="212" y="70">1/6/2002</text><text x="185" y="186">1/7/2002</text><text x="34" y="186">1/8/2002</text><text x="2" y="70">1/9/2002</text></g>
    </svg>
    <svg class="wave"><use href="#wave"/></svg>
    <span class="pageno">17</span><span class="url">www.velmoro.at</span>
  </section>

  <!-- 18 comparison -->
  <section class="slide">
    <div class="date">01/02/2020</div><div class="badge"></div>
    <h2 class="title">Gegenüberstellungen</h2>
    <div class="cmp-head" style="left:100px">Vor</div>
    <div class="cmp-head" style="left:313px">Nachteile</div>
    <div class="cmp-row" style="left:58px;top:104px"><span class="ico blue"><svg><use href="#i-cal"/></svg></span><div><h4>Adipiscing Elit</h4><p>Quisque iaculis dolor vel ipsum rutrum mattis. Phasellus tristique ante et nibh mollis consequat. Donec id elit in arcu laoreet vulputate.</p></div></div>
    <div class="cmp-row" style="left:58px;top:156px"><span class="ico blue"><svg><use href="#i-card"/></svg></span><div><h4>Nulla Facilisi</h4><p>Quisque iaculis dolor vel ipsum rutrum mattis. Phasellus tristique ante et nibh mollis consequat. Donec id elit in arcu laoreet vulputate.</p></div></div>
    <div class="cmp-row" style="left:58px;top:207px"><span class="ico dark"><svg><use href="#i-case"/></svg></span><div><h4>Faucibus Sapien</h4><p>Quisque iaculis dolor vel ipsum rutrum mattis. Phasellus tristique ante et nibh mollis consequat. Donec id elit in arcu laoreet vulputate.</p></div></div>
    <div class="cmp-row" style="left:272px;top:104px"><span class="ico blue"><svg><use href="#i-cal"/></svg></span><div><h4>Adipiscing Elit</h4><p>Quisque iaculis dolor vel ipsum rutrum mattis. Phasellus tristique ante et nibh mollis consequat. Donec id elit in arcu laoreet vulputate.</p></div></div>
    <div class="cmp-row" style="left:272px;top:156px"><span class="ico blue"><svg><use href="#i-card"/></svg></span><div><h4>Nulla Facilisi</h4><p>Quisque iaculis dolor vel ipsum rutrum mattis. Phasellus tristique ante et nibh mollis consequat. Donec id elit in arcu laoreet vulputate.</p></div></div>
    <div class="cmp-row" style="left:272px;top:207px"><span class="ico dark"><svg><use href="#i-case"/></svg></span><div><h4>Faucibus Sapien</h4><p>Quisque iaculis dolor vel ipsum rutrum mattis. Phasellus tristique ante et nibh mollis consequat. Donec id elit in arcu laoreet vulputate.</p></div></div>
    <svg class="wave"><use href="#wave"/></svg>
    <span class="pageno">18</span><span class="url">www.velmoro.at</span>
  </section>

</main>
</body>
</html>
```